Peer-to-peer Car Rental Business needs a business card design

We need a business card design for a new company based in Melbourne, Australia called "Wheelnest". We enable car owners to earny money by renting out their car to others in the community/neighbourhood when their not using it.
We would like to see designs that use the colour/s blue and/or orange.
The design should communicate young, modern, fun etc.
The themes to use should be community/neighbourhood, cars, parking, airports, car rental, sharing.

Our current logo is attached.

Target Market(s)

Young adults aged 20-35, travellers, environmentally conscious, cost conscious.

Industry/Entity Type

Business

Requirements
Must have
• Must have fields for persons name, title, mobile number, email company website.

```html
<!DOCTYPE html>
<html lang="en">
<head>
<meta charset="utf-8">
<title>Wheelnest Business Card</title>
<link href="https://fonts.googleapis.com/css2?family=Arimo:wght@400&family=Tinos:wght@700&display=swap" rel="stylesheet">
<style>
  :root {
    --navy: #2c2a86;
    --mid-blue: #1f56b0;
    --sky: #0a8fd6;
    --headline-yellow: #f4e613;
    --city-yellow: #e9ef3a;
    --brand-ink: #2e3d8c;
    --white: #ffffff;
    --page: #ffffff;
    --art-tint-a: rgba(255, 255, 255, 0.10);
    --art-tint-b: rgba(255, 255, 255, 0.04);
  }
  * { margin: 0; padding: 0; box-sizing: border-box; }
  html, body {
    width: 886px;
    height: 1200px;
    overflow: hidden;
    background: var(--page);
  }
  .sheet {
    position: relative;
    width: 886px;
    height: 1200px;
  }
  .card {
    position: absolute;
    left: 0;
    width: 886px;
    height: 512px;
    background: linear-gradient(100deg, var(--navy) 0%, var(--mid-blue) 55%, var(--sky) 100%);
    overflow: hidden;
  }
  .card--front { top: 0; }
  .card--back { top: 688px; }

  .brand-strip {
    position: absolute;
    top: 19px;
    left: 572px;
    width: 314px;
    height: 63px;
    background: linear-gradient(90deg, rgba(255,255,255,0) 0%, rgba(255,255,255,0.85) 18%, var(--white) 40%);
    display: flex;
    align-items: center;
    justify-content: flex-end;
    padding-right: 22px;
  }
  .brand-name {
    font-family: "Arimo", Arial, sans-serif;
    font-weight: 400;
    font-size: 44px;
    letter-spacing: 0.5px;
    color: var(--brand-ink);
    line-height: 1;
  }
  .brand-city {
    position: absolute;
    top: 96px;
    left: 610px;
    width: 260px;
    text-align: center;
    font-family: "Tinos", "Times New Roman", serif;
    font-weight: 700;
    font-size: 21px;
    color: var(--city-yellow);
  }

  .car-art {
    position: absolute;
    left: 58px;
    top: 66px;
    width: 745px;
    height: 282px;
    border-radius: 150px 150px 12px 12px;
    background: linear-gradient(180deg, var(--art-tint-a) 0%, var(--art-tint-b) 100%);
  }
  .headline {
    position: absolute;
    top: 374px;
    left: 0;
    width: 870px;
    text-align: center;
    font-family: "Tinos", "Times New Roman", serif;
    font-weight: 700;
    font-size: 72px;
    line-height: 1;
    color: var(--headline-yellow);
    letter-spacing: 1px;
  }

  .contact-fields {
    position: absolute;
    top: 150px;
    left: 75px;
    width: 735px;
    list-style: none;
    font-family: "Arimo", Arial, sans-serif;
    font-size: 37px;
    color: var(--white);
  }
  .field {
    display: flex;
    align-items: flex-end;
    height: 54px;
    white-space: pre;
  }
  .field-label { line-height: 1; }
  .field-line {
    flex: 1;
    border-bottom: 2px solid var(--white);
    margin-left: 6px;
    margin-bottom: 2px;
  }
  .field--blank { height: 52px; }
  .field--blank .field-line { margin-left: 0; }
</style>
</head>
<body>
<div class="sheet">

  <section class="card card--front">
    <div class="brand-strip"><span class="brand-name">Wheelnest</span></div>
    <p class="brand-city">Melbourne, Australia</p>

    <div class="car-art" role="img" aria-label="White line illustration of a small car seen from the side"></div>

    <h1 class="headline">CAR FOR RENT</h1>
  </section>

  <section class="card card--back">
    <div class="brand-strip"><span class="brand-name">Wheelnest</span></div>
    <p class="brand-city">Melbourne, Australia</p>

    <ul class="contact-fields">
      <li class="field"><span class="field-label">Name :</span><span class="field-line"></span></li>
      <li class="field"><span class="field-label">Title    :</span><span class="field-line"></span></li>
      <li class="field"><span class="field-label">Mobile number :</span><span class="field-line"></span></li>
      <li class="field"><span class="field-label">E-mail :</span><span class="field-line"></span></li>
      <li class="field"><span class="field-label">Company website :</span><span class="field-line"></span></li>
      <li class="field field--blank"><span class="field-line"></span></li>
    </ul>
  </section>

</div>
</body>
</html>
```